Allied Health team of Physiotherapists & Occupational Therapists seek a business card design

We have our new logo, we now need our new business cards and stationary. Blossom: Lymphoedema & Women's Clinic is seeking a generic card design to represent our whole team and individual cards for each therapist that incorporates our new logo to communicate our holistic approach that is calming, nuturing, supportive and welcoming.
Our Physiotherapists and Occupational Therapists assess, treat and provide education for people who are at risk of or who have lymphoedema. This is often as a result of treatment for cancer. We provide pre-operative and post-operative management and cancer rehabilitation in our Pilates studio. Our team also consists of Physiotherapists who have a strong interest in pelvic floor and continence management for both men and women.

Target Market(s)

Mainly women health conscious

Industry/Entity Type

Allied Health: Physiotherapy / Occupational Therapy

Contact Information for Business Card

Address: 14 Calloway Ave Fernvale 3288 Phone: 84317560 fax: 8431 7564 Email: info@blossomcarepartners.com.au Website: blossomcarepartners.com.au Facebook address: facebook.com/BlossomLymphoedemaAndWomensCareCentre. Room to write appointments. Individual cards need to have name, office email and individual email and professional details

Requirements
Must have
• Logo as per uploaded documents

```html
<!DOCTYPE html>
<html lang="en">
<head>
<meta charset="utf-8">
<title>Blossom Business Card</title>
<link rel="stylesheet" href="https://fonts.googleapis.com/css2?family=Barlow:ital,wght@0,400;0,500;0,600;1,500&family=Philosopher:wght@700&display=swap">
<style>
  :root {
    --stage: #080808;
    --cream: #fefbd7;
    --peach: #f9b07f;
    --peach-light: #fcd3aa;
    --sage: #c1cbbe;
    --ink: #2a2a26;
    --ink-soft: #45453f;
    --white: #fffdf0;
  }
  * { box-sizing: border-box; margin: 0; padding: 0; }
  html, body {
    width: 1200px; height: 892px; overflow: hidden;
    background: var(--stage);
    font-family: "Barlow", Arial, sans-serif;
  }
  .canvas { position: relative; width: 1200px; height: 892px; }
  .card {
    position: absolute; width: 502px; height: 287px; overflow: hidden;
  }
  .card--front { left: 223px; top: 121px; background: var(--cream); }
  .card--back  { left: 475px; top: 483px; background: var(--peach); }

  .brand-panel {
    position: absolute; left: 0; top: 0; width: 175px; height: 250px;
    border-bottom-right-radius: 8px; z-index: 2;
    display: flex; align-items: center; justify-content: center;
  }
  .brand-tab {
    position: absolute; left: 0; top: 0; width: 153px; height: 270px;
    border-bottom-right-radius: 8px; z-index: 1;
  }
  .card--front .brand-panel { background: var(--peach); }
  .card--front .brand-tab { background: var(--sage); }
  .card--back .brand-panel { background: var(--cream); }
  .card--back .brand-tab { background: var(--peach-light); }

  .brand-name {
    font-family: "Barlow", Arial, sans-serif;
    font-weight: 500; font-size: 30px; letter-spacing: 0.5px;
  }
  .card--front .brand-name { color: var(--cream); }
  .card--back .brand-name { color: var(--peach); }

  .person { position: absolute; left: 213px; top: 45px; }
  .person__name {
    font-family: "Philosopher", Georgia, serif; font-weight: 700;
    font-size: 20px; color: var(--ink); letter-spacing: 0.2px;
  }
  .person__role {
    font-style: italic; font-weight: 500; font-size: 13.5px;
    color: var(--ink-soft); margin-top: 2px;
  }
  .services {
    position: absolute; left: 213px; top: 176px; list-style: none;
    font-weight: 600; font-size: 12px; color: var(--ink); line-height: 20px;
  }

  .contacts {
    position: absolute; left: 227px; top: 35px; list-style: none;
    color: var(--white); font-size: 14px; line-height: 20px;
  }
  .contacts li { display: flex; align-items: center; gap: 5px; }
  .contacts .phone { letter-spacing: 1px; }
  .contacts svg { width: 14px; height: 14px; flex: none; }

  .appointment {
    position: absolute; left: 227px; top: 153px;
    color: var(--white); font-weight: 600; font-size: 15px;
    display: flex; align-items: baseline; gap: 4px;
  }
  .appointment__line {
    display: inline-block; width: 112px; border-bottom: 1.5px dotted var(--white);
  }
  .divider {
    position: absolute; left: 227px; right: 0; top: 189px;
    border-top: 1px solid var(--white); opacity: 0.85;
  }
  .booking { position: absolute; left: 227px; top: 217px; color: var(--white); }
  .booking__label { font-weight: 600; font-size: 13.5px; }
  .booking__url { font-size: 15.5px; letter-spacing: 0.3px; margin-top: -1px; }
</style>
</head>
<body>
<main class="canvas">

  <section class="card card--front" aria-label="Business card front">
    <div class="brand-tab"></div>
    <div class="brand-panel"><span class="brand-name">Blossom</span></div>
    <div class="person">
      <h1 class="person__name">Maren Holt</h1>
      <p class="person__role">Physiotherapist</p>
    </div>
    <ul class="services">
      <li>Lymphoedema &amp; Oncology Rehabilitation</li>
      <li>Continence &amp; Pelvic Floor</li>
    </ul>
  </section>

  <section class="card card--back" aria-label="Business card back">
    <div class="brand-tab"></div>
    <div class="brand-panel"><span class="brand-name">Blossom</span></div>

    <ul class="contacts">
      <li class="phone">
        <svg viewBox="0 0 14 14"><circle cx="7" cy="7" r="6.2" fill="none" stroke="#fffdf0" stroke-width="1.2"/><path d="M4.6 3.8c.4-.3.8-.2 1 .2l.6 1.1c.2.3.1.6-.2.8l-.4.3c.3.8 1 1.5 1.8 1.9l.3-.4c.2-.3.5-.3.8-.2l1.1.6c.4.2.4.6.2 1-.5.8-1.3 1-2.1.6C6.1 9 4.9 7.800 4.3 6.2c-.3-.9-.1-1.7.3-2.4z" fill="#fffdf0"/></svg>
        8431 7560
      </li>
      <li class="phone">
        <svg viewBox="0 0 14 14"><circle cx="7" cy="7" r="6.5" fill="#fffdf0"/><rect x="4" y="5.3" width="6" height="4.4" rx=".6" fill="#f9b07f"/><rect x="5" y="3.8" width="4" height="2" fill="#f9b07f"/></svg>
        8431 7564
      </li>
      <li>
        <svg viewBox="0 0 14 14"><circle cx="7" cy="7" r="6.5" fill="#fffdf0"/><rect x="3.8" y="4.8" width="6.4" height="4.4" rx=".5" fill="#f9b07f"/><path d="M3.9 5l3.1 2.3L10.1 5" fill="none" stroke="#fffdf0" stroke-width=".8"/></svg>
        info@blossomcarepartners.com.au
      </li>
      <li>
        <svg viewBox="0 0 14 14"><circle cx="7" cy="7" r="6.5" fill="#fffdf0"/><path d="M7 3.2a2.6 2.6 0 0 0-2.6 2.6C4.4 7.8 7 10.8 7 10.8s2.6-3 2.6-5A2.6 2.6 0 0 0 7 3.2z" fill="#f9b07f"/><circle cx="7" cy="5.8" r="1" fill="#fffdf0"/></svg>
        14 Calloway Ave, Fernvale 3288
      </li>
    </ul>

    <p class="appointment">Next Appointment <span class="appointment__line"></span></p>
    <div class="divider"></div>

    <div class="booking">
      <p class="booking__label">Book Online</p>
      <p class="booking__url">www.blossomcarepartners.com.au</p>
    </div>
  </section>

</main>
</body>
</html>
```